Web Design Business Card

I need a new business card designed, we recently rebranded and I need to get a fresh design to match our new logo, colours and branding.

Details:

Dorian Keeble | Founder & CEO
Address: 7 Fernhollow Lane, #04-09 Maplecrest Vale, Singapore 583104
Tel: +65 93468120
Web: www.plumtrove.com.sg
hello@plumtrove.com.sg

I've attached my old card as well

Requirements
Must have
• Front and Back
Interesting use of logo
Correct use of colour scheme

```html
<!DOCTYPE html>
<html lang="en">
<head>
<meta charset="utf-8">
<title>Plumtrove Business Card</title>
<link href="https://fonts.googleapis.com/css2?family=Open+Sans:wght@400;600;700&display=swap" rel="stylesheet">
<style>
  :root {
    --stage: #3d3c3e;
    --back-centre: #a09083;
    --back-edge: #74655a;
    --mark-dark: #6d5d52;
    --wordmark: #7a6a60;
    --ink: #4f4f4f;
    --muted: #6a6a6a;
    --accent-brown: #a48c78;
    --icon: #8c7d73;
    --blue: #1aa6e6;
    --blue-light: #5fcaf5;
    --rule-brown: #7c6d65;
    --white: #ffffff;
  }
  * { margin: 0; padding: 0; box-sizing: border-box; }
  html, body { width: 1200px; height: 372px; overflow: hidden; }
  body { background: var(--stage); position: relative; font-family: "Open Sans", Arial, sans-serif; }

  .card { position: absolute; width: 542px; height: 288px; overflow: hidden; }

  .card--back {
    left: 47px; top: 33px;
    background: radial-gradient(ellipse at 45% 42%, var(--back-centre) 0%, var(--back-edge) 75%);
  }
  .card--front { left: 609px; top: 35px; background: var(--white); }

  .brand { position: absolute; display: flex; align-items: center; }
  .brand__dot { border-radius: 50%; flex: none; }
  .brand__name { font-weight: 700; letter-spacing: -0.6px; line-height: 1; white-space: nowrap; }

  .card--back .brand { left: 130px; top: 102px; }
  .card--back .brand__dot { width: 73px; height: 73px; background: var(--mark-dark); margin-right: 16px; }
  .card--back .brand__name { font-size: 38px; color: var(--mark-dark); }

  .card--front .brand { left: 39px; top: 110px; }
  .card--front .brand__dot {
    width: 74px; height: 74px; margin-right: 6px;
    background: linear-gradient(160deg, var(--blue) 0%, var(--blue-light) 100%);
  }
  .card--front .brand__name { font-size: 34px; color: var(--wordmark); }

  .divider {
    position: absolute; left: 312px; top: 56px; height: 158px;
    border-left: 2px dashed var(--icon);
  }

  .contact { position: absolute; left: 355px; top: 55px; color: var(--muted); }
  .contact__name { font-size: 16px; color: var(--ink); line-height: 22px; }
  .contact__role { font-size: 12px; color: var(--accent-brown); line-height: 16px; }

  .contact__row { position: absolute; left: 0; font-size: 14px; line-height: 20px; white-space: nowrap; }
  .contact__row--address { top: 52px; }
  .contact__row--phone { top: 120px; }
  .contact__row--mail { top: 141px; }
  .contact__indent { padding-left: 4px; }

  .icon { position: absolute; left: -28px; fill: var(--icon); }
  .contact__row--address .icon { top: 2px; }
  .contact__row--phone .icon { top: 1px; }
  .contact__row--mail .icon { top: 4px; }

  .footer-rule { position: absolute; left: 0; top: 271px; width: 350px; height: 4px; background: var(--rule-brown); }
  .footer-band { position: absolute; left: 0; top: 278px; width: 542px; height: 10px; background: var(--blue); }
  .footer-tab {
    position: absolute; left: 343px; top: 265px; width: 199px; height: 23px;
    background: var(--blue); border-top-left-radius: 22px 16px;
  }
  .footer-web {
    position: absolute; right: 21px; top: 268px;
    font-size: 12.5px; font-weight: 700; color: var(--white); line-height: 18px;
  }
</style>
</head>
<body>
  <section class="card card--back" aria-label="Card back">
    <div class="brand">
      <span class="brand__dot"></span>
      <span class="brand__name">plumtrove</span>
    </div>
  </section>

  <section class="card card--front" aria-label="Card front">
    <div class="brand">
      <span class="brand__dot"></span>
      <span class="brand__name">plumtrove</span>
    </div>

    <div class="divider"></div>

    <div class="contact">
      <p class="contact__name">Dorian Keeble</p>
      <p class="contact__role">Founder &amp; CEO</p>

      <p class="contact__row contact__row--address">
        <svg class="icon" width="13" height="18" viewBox="0 0 13 18" aria-hidden="true">
          <path d="M6.5 0A6.5 6.5 0 0 0 0 6.5C0 11 6.5 18 6.5 18S13 11 13 6.5A6.5 6.5 0 0 0 6.5 0Zm0 9.2a2.7 2.7 0 1 1 0-5.4 2.7 2.7 0 0 1 0 5.4Z"/>
        </svg>
        7 Fernhollow Lane,<br>
        <span class="contact__indent">#04-09 Maplecrest Vale,</span><br>
        Singapore 583104
      </p>

      <p class="contact__row contact__row--phone">
        <svg class="icon" width="18" height="18" viewBox="0 0 18 18" aria-hidden="true">
          <path d="M4 1 7 5 5.3 7.2a10 10 0 0 0 5.5 5.5L13 11l4 3-1.8 2.6C14.4 17.8 6 15 3 11 .5 7.7 0 4.5 1.4 2.8Z"/>
        </svg>
        +65 93468120
      </p>

      <p class="contact__row contact__row--mail">
        <svg class="icon" width="18" height="13" viewBox="0 0 18 13" aria-hidden="true">
          <path d="M0 0h18v13H0Zm1.6 1.5v.3L9 7.3l7.4-5.5v-.3Zm0 2.2v7.8h14.8V3.7L9 9.2Z"/>
        </svg>
        hello@plumtrove.com.sg
      </p>
    </div>

    <div class="footer-rule"></div>
    <div class="footer-band"></div>
    <div class="footer-tab"></div>
    <p class="footer-web">www.plumtrove.com.sg</p>
  </section>
</body>
</html>
```